Brisco Home Residential cleaning services- Opening Flyer

1. I would like to have flyer design offering the hourly rate residential cleaning normal rate will be 35 AED per hour.
2. I want to have a special opening rate which is less than 25 AED which is equivalent to 30% Off.This opening offer will be limited time
We have a different cleaning packages like "Basic , Deep, And custom"
3. Also we have different types contracts Yearly/Monthly/Weekly and daily.
4. we are providing cleaning material and cleaning equipment upon request.And all the material used are environmental friendly.
5. Our customers mostly will be house wives.
6. Our service will be available in Ruwais city.
7. I would like to have a modern attractive flyer, i like it to be smart in its colors and the psychology of the customers.
8. I like to have attractive statements like " Now Available in Ruwais" and other statements from your own.
9. I will attach my logo design and if you need any other uploads let me know.
10. Our slogan is "Experience the Difference"
11. Paper size , i expect to be A5 (210mm x 148mm).
12. I am expecting the flyer to be single size as it will translated to another language in the other side.
13. please use the statement also ( less than 25 AED)
14. Do the arrangement you can see to the flyer statements as to look professional and comfortable to read.
15. Company web site is " www.briscohome.ae"
16. company email " support@briscohome.ae"
17. I will update you with contact number soon
18. My contacts are
Support@briscohome.ae
+971 508817345
+971 508817347
19. Update some slogans to be used

```html
<!DOCTYPE html>
<html lang="en">
<head>
<meta charset="utf-8">
<title>Brisco Home – Opening Flyer</title>
<link rel="stylesheet" href="https://fonts.googleapis.com/css2?family=Lato:wght@400;700;900&family=Oswald:wght@500;700&family=Roboto+Condensed:wght@700&display=swap">
<style>
  :root{
    --blue:#1d7fc4;
    --blue-dark:#0d4f86;
    --blue-light:#3aa5e0;
    --green:#8cc63f;
    --green-dark:#5d9a1c;
    --lime:#c8e03a;
    --ink:#222;
    --text:#333;
    --white:#fff;
    --stage:#e6e6e6;
  }
  html,body{margin:0;padding:0;}
  body{width:995px;height:1200px;overflow:hidden;background:var(--stage);position:relative;font-family:"Lato",sans-serif;}
  .flyer{position:absolute;left:77px;top:12px;width:840px;height:1176px;background:var(--white);overflow:hidden;box-shadow:0 2px 10px rgba(0,0,0,.15);}
  .flyer__shapes{position:absolute;inset:0;}
  .worker-photo{position:absolute;left:540px;top:800px;width:240px;height:376px;border-radius:40px 40px 0 0;background:linear-gradient(180deg,rgba(40,90,200,.55),rgba(30,30,40,.55));}
  .tagline{position:absolute;left:0;top:414px;width:394px;height:108px;box-sizing:border-box;border:3px solid #2b3a12;border-left:none;border-radius:0 30px 30px 0;background:linear-gradient(180deg,#9fd24a,var(--green-dark));color:var(--white);padding:14px 0 0 38px;}
  .tagline__lead{font:900 33px/1 "Lato",sans-serif;color:#16240a;}
  .tagline__sub{font:900 23px/1.2 "Lato",sans-serif;margin-top:6px;}
  .tab{position:absolute;left:0;height:48px;background:linear-gradient(180deg,var(--blue-light),var(--blue-dark));color:var(--white);border-radius:0 24px 24px 0;font:700 28px/48px "Roboto Condensed",sans-serif;padding-left:36px;box-sizing:border-box;}
  .tab--packages{top:548px;width:315px;}
  .tab--about{top:678px;width:185px;}
  .packages{position:absolute;left:38px;top:610px;font:700 24px/1 "Lato",sans-serif;color:var(--ink);display:flex;gap:14px;}
  .packages span::before{content:"";display:inline-block;width:9px;height:9px;border-radius:50%;background:var(--green);margin-right:8px;vertical-align:middle;}
  .contracts{position:absolute;left:38px;top:644px;margin:0;font:700 16px/18px "Lato",sans-serif;color:var(--blue-dark);}
  .about{position:absolute;left:39px;top:750px;width:400px;margin:0;font:400 21.5px/30px "Lato",sans-serif;color:var(--text);}
  .brand{position:absolute;left:500px;top:432px;display:flex;align-items:center;gap:14px;}
  .brand__dot{width:36px;height:36px;border-radius:50%;background:var(--blue);}
  .brand__name{font:900 40px/1 "Lato",sans-serif;color:var(--blue);}
  .slogan{position:absolute;left:460px;width:340px;text-align:center;margin:0;}
  .slogan--main{top:558px;font:700 62px/1 "Oswald",sans-serif;color:var(--blue);letter-spacing:1px;}
  .slogan--sub{top:620px;font:700 41px/1 "Oswald",sans-serif;color:var(--lime);-webkit-text-stroke:1px var(--green-dark);}
  .pitch{position:absolute;left:460px;width:340px;text-align:center;margin:0;}
  .pitch--main{top:680px;font:900 33px/1 "Lato",sans-serif;color:var(--ink);}
  .pitch--sub{top:718px;font:700 22px/1 "Roboto Condensed",sans-serif;color:var(--blue);}
  .pitch--area{top:750px;font:900 19px/1 "Lato",sans-serif;color:var(--green-dark);}
  .offer{position:absolute;left:335px;top:887px;width:188px;height:188px;border-radius:50%;text-align:center;color:var(--white);}
  .offer__lead{margin-top:34px;font:700 21px/1 "Lato",sans-serif;}
  .offer__price{font:700 42px/1 "Oswald",sans-serif;color:var(--lime);margin-top:5px;}
  .offer__save{font:900 18px/1 "Lato",sans-serif;margin-top:6px;}
  .offer__normal{font:700 13px/1 "Lato",sans-serif;margin-top:5px;opacity:.9;}
  .contacts{position:absolute;left:34px;top:1002px;margin:0;padding:0;list-style:none;}
  .contacts li{display:flex;align-items:center;gap:16px;height:40px;font:700 24px/1 "Lato",sans-serif;color:#10306a;}
  .contacts svg{width:20px;height:20px;fill:var(--blue-dark);}
</style>
</head>
<body>
<main class="flyer">
  <svg class="flyer__shapes" viewBox="0 0 840 1176" width="840" height="1176">
    <defs>
      <linearGradient id="sand" x1="0" y1="0" x2="0" y2="1">
        <stop offset="0" stop-color="#dfe8f0"/>
        <stop offset=".35" stop-color="#cdbd9c"/>
        <stop offset="1" stop-color="#b39a74"/>
      </linearGradient>
      <linearGradient id="meadow" x1="0" y1="0" x2="0" y2="1">
        <stop offset="0" stop-color="#9fd24a"/>
        <stop offset="1" stop-color="#7ab52c"/>
      </linearGradient>
      <linearGradient id="band" x1="0" y1="0" x2="1" y2="0">
        <stop offset="0" stop-color="#3aa5e0"/>
        <stop offset="1" stop-color="#0d4f86"/>
      </linearGradient>
      <radialGradient id="badge" cx=".5" cy=".4" r=".6">
        <stop offset="0" stop-color="#3aa5e0"/>
        <stop offset="1" stop-color="#0d5c9c"/>
      </radialGradient>
    </defs>
    <path role="img" aria-label="Photo of a family playing in the sand on a sunny beach" d="M0 0H840V450C600 330 260 320 0 380Z" fill="url(#sand)"/>
    <path d="M0 380C260 320 600 330 840 450V478C600 355 260 345 0 402Z" fill="url(#band)"/>
    <path d="M0 410C260 352 600 362 840 486" fill="none" stroke="#9fd0ee" stroke-width="3"/>
    <path d="M0 925C220 1005 470 990 840 810V1176H0Z" fill="url(#meadow)"/>
    <path d="M0 915C220 995 470 980 840 800" fill="none" stroke="#1d7fc4" stroke-width="4"/>
    <path d="M330 1012C560 985 720 880 840 760V835C700 940 540 1010 330 1012Z" fill="url(#band)"/>
    <circle cx="429" cy="981" r="94" fill="url(#badge)" stroke="#fff" stroke-width="8"/>
  </svg>

  <div class="worker-photo" role="img" aria-label="Photo of a cleaner in a blue shirt vacuuming a carpet"></div>

  <div class="tagline">
    <div class="tagline__lead">A CLEAN HOME IS A</div>
    <div class="tagline__sub">HEALTHY AND HAPPY HOME</div>
  </div>

  <div class="brand">
    <span class="brand__dot"></span>
    <span class="brand__name">Brisco Home</span>
  </div>

  <h1 class="slogan slogan--main">EXPERIENCE</h1>
  <h2 class="slogan slogan--sub">THE DIFFERENCE</h2>
  <p class="pitch pitch--main">NO MORE CLEANING</p>
  <p class="pitch pitch--sub">LET THE PROFESSIONALS DO IT</p>
  <p class="pitch pitch--area">NOW AVAILABLE IN RUWAIS</p>

  <div class="tab tab--packages">CLEANING PACKAGES</div>
  <div class="packages"><span>BASIC</span><span>DEEP</span><span>CUSTOM</span></div>
  <p class="contracts">Contracts: Yearly • Monthly • Weekly • Daily</p>

  <div class="tab tab--about">ABOUT US</div>
  <p class="about">We are providing cleaning material and cleaning equipment upon request.And all the material used are environmental friendly. Our service will be available in Ruwais city.</p>

  <div class="offer">
    <div class="offer__lead">LESS THAN</div>
    <div class="offer__price">25 AED</div>
    <div class="offer__save">30% OFF</div>
    <div class="offer__normal">Normal rate 35 AED/hr</div>
  </div>

  <ul class="contacts">
    <li><svg viewBox="0 0 24 24"><path d="M6.6 10.8a15 15 0 0 0 6.6 6.6l2.2-2.2c.3-.3.7-.4 1-.2 1.1.4 2.3.6 3.6.6.6 0 1 .4 1 1V20c0 .6-.4 1-1 1C10.6 21 3 13.4 3 4c0-.6.4-1 1-1h3.5c.6 0 1 .4 1 1 0 1.3.2 2.5.6 3.6.1.3 0 .7-.2 1z"/></svg>+971 508817345</li>
    <li><svg viewBox="0 0 24 24"><path d="M6.6 10.8a15 15 0 0 0 6.6 6.6l2.2-2.2c.3-.3.7-.4 1-.2 1.1.4 2.3.6 3.6.6.6 0 1 .4 1 1V20c0 .6-.4 1-1 1C10.6 21 3 13.4 3 4c0-.6.4-1 1-1h3.5c.6 0 1 .4 1 1 0 1.3.2 2.5.6 3.6.1.3 0 .7-.2 1z"/></svg>+971 508817347</li>
    <li><svg viewBox="0 0 24 24"><circle cx="12" cy="12" r="10" fill="none" stroke="#0d4f86" stroke-width="2"/><ellipse cx="12" cy="12" rx="4" ry="10" fill="none" stroke="#0d4f86" stroke-width="2"/><path d="M2 12h20" stroke="#0d4f86" stroke-width="2"/></svg>www.briscohome.ae</li>
    <li><svg viewBox="0 0 24 24"><path d="M2 5h20v14H2z"/><path d="M2 5l10 8 10-8" fill="none" stroke="#fff" stroke-width="1.6"/></svg>support@briscohome.ae</li>
  </ul>
</main>
</body>
</html>
```